Graphic Design for a Info Card

We would like a graphic design for an info card . We would like the colours to correspond to our logo , you can add in the colours navy blue or yellow if you would like. We would like it to have the following information. We want something that really pops. We would like the size to be 4 1/2 x 6 .

ATTENTION!! Delivery Promo! Order from us on the @hopmorsel app or @vantrelcourier app on FRIDAYS and receive a FREE Sample of our one of our meal prep meals in your bag!
DID YOU KNOW?! Meal Prep is another great service that we offer. Saving you time, promoting your health, and best of all providing a delicious lunch . You can find more info on our website www.marlowpantry.example . All orders are available for delivery or pickup!

```html
<!DOCTYPE html>
<html lang="en">
<head>
<meta charset="utf-8">
<title>Marlow Pantry – Delivery Promo Info Card</title>
<link href="https://fonts.googleapis.com/css2?family=Catamaran:wght@500;600;700;800&family=Allura&display=swap" rel="stylesheet">
<style>
  :root {
    --navy: #1c3661;
    --green: #8cc43f;
    --green-dark: #76ad2c;
    --lime: #a4d93a;
    --grey: #9b9b9b;
    --grey-text: #7d7d7d;
    --orange: #f47b20;
    --white: #ffffff;
    --stage: #0d0d0d;
  }
  * { box-sizing: border-box; margin: 0; padding: 0; }
  html, body { width: 1200px; height: 1200px; overflow: hidden; background: var(--stage); }
  body { font-family: "Catamaran", sans-serif; }
  .card {
    position: absolute; left: 208px; top: 71px;
    width: 731px; height: 975px;
    transform: scale(1.0909); transform-origin: top left;
    background: var(--white); overflow: hidden;
  }
  .abs { position: absolute; white-space: nowrap; }
  .top-left { left: 0; top: 0; width: 310px; height: 77px; background: var(--navy);
    color: var(--white); font-weight: 800; font-size: 40px; display: flex; align-items: center; justify-content: center; }
  .top-right { left: 310px; top: 0; width: 421px; height: 77px; background: var(--grey);
    color: var(--white); font-weight: 700; font-size: 36px; display: flex; align-items: center; justify-content: center; }
  .promo-ribbon { left: 21px; top: 77px; }
  .promo-title { left: 21px; width: 289px; text-align: center; color: var(--white); font-weight: 800; }
  .promo-title.big { top: 152px; font-size: 50px; line-height: 1; }
  .promo-title.small { top: 205px; font-size: 36px; line-height: 1; display: flex; align-items: center; justify-content: center; gap: 8px; }
  .promo-title.small::before, .promo-title.small::after { content: ""; width: 38px; height: 2px; background: var(--white); }
  .app-tile { top: 87px; width: 75px; height: 75px; border: 3px solid var(--navy); border-radius: 6px; padding: 3px; background: var(--white); }
  .app-tile span { display: flex; width: 100%; height: 100%; background: var(--orange); border-radius: 3px;
    color: var(--white); font-weight: 700; font-size: 12px; align-items: center; justify-content: center; }
  .script { font-family: "Allura", cursive; }
  .or { left: 503px; top: 100px; font-size: 36px; color: var(--navy); }
  .handle { top: 172px; width: 190px; text-align: center; color: var(--navy); font-weight: 600; font-size: 19px; line-height: 22px; }
  .receive { left: 353px; top: 228px; color: var(--navy); font-weight: 700; font-size: 24px; }
  .receive b, .pill b { color: var(--lime); font-weight: 800; }
  .receive b { font-size: 31px; }
  .pill { left: 353px; top: 267px; width: 325px; height: 37px; border-radius: 19px; background: var(--navy);
    color: var(--white); font-weight: 800; font-size: 30px; display: flex; align-items: center; justify-content: center; padding-top: 3px; }
  .sample-note { left: 351px; top: 306px; color: var(--navy); font-weight: 600; font-size: 23px; line-height: 28px; }
  .sample-note b { font-weight: 800; }
  .meals-photo { left: 355px; top: 368px; width: 376px; height: 355px; }
  .know { left: 142px; top: 455px; color: var(--white); font-size: 50px; }
  .mealprep { left: 43px; top: 526px; width: 328px; height: 72px; border: 3px solid var(--white);
    font-weight: 800; font-size: 52px; line-height: 1; color: var(--white); padding: 12px 0 0 10px; }
  .mealprep span { color: var(--navy); }
  .service { left: 62px; top: 605px; color: var(--white); font-weight: 600; font-size: 23px; line-height: 27px; }
  .benefit { top: 676px; width: 108px; }
  .benefit .ring { position: absolute; left: 13px; top: 0; width: 82px; height: 82px; border-radius: 50%;
    background: var(--white); border: 4px solid var(--green-dark); box-shadow: 0 0 0 3px var(--white); }
  .benefit .ring svg { position: absolute; left: 14px; top: 14px; }
  .benefit .label { position: absolute; left: 0; top: 71px; width: 108px; height: 64px; background: var(--navy);
    color: var(--white); font-weight: 700; font-size: 17px; line-height: 20px; text-align: center; padding-top: 16px; }
  .info-tab { left: 477px; top: 785px; width: 254px; height: 51px; background: var(--navy); border-radius: 26px 0 0 0;
    color: var(--white); font-size: 40px; padding: 4px 0 0 42px; }
  .brand { left: 31px; top: 856px; width: 272px; text-align: center; color: var(--grey-text); font-weight: 800; font-size: 29px; line-height: 1; }
  .brand-sub { left: 31px; top: 892px; width: 272px; text-align: center; color: var(--green-dark); font-weight: 700; font-size: 15px; letter-spacing: .3px; }
  .web { left: 326px; top: 850px; width: 388px; text-align: center; color: var(--grey-text); font-weight: 800; font-size: 21px; line-height: 30px; }
  .social { top: 882px; width: 32px; height: 32px; border-radius: 50%; background: var(--green-dark); }
  .footer-band { left: 0; top: 927px; width: 731px; height: 48px; background: var(--grey);
    display: flex; align-items: center; justify-content: center; gap: 14px;
    color: var(--white); font-style: italic; font-weight: 600; font-size: 23px; }
  .footer-band::before, .footer-band::after { content: ""; width: 110px; height: 2px; background: var(--white); }
</style>
</head>
<body>
<main class="card">
  <div class="abs top-left">ATTENTION!</div>
  <div class="abs top-right">ORDER FROM US ON</div>

  <svg class="abs promo-ribbon" width="289" height="248" viewBox="0 0 289 248">
    <polygon points="0,0 289,0 289,168 0,248" fill="var(--green)"/>
    <g fill="var(--white)">
      <rect x="70" y="25" width="26" height="3" rx="1.5"/>
      <rect x="64" y="33" width="28" height="3" rx="1.5"/>
      <rect x="74" y="41" width="20" height="3" rx="1.5"/>
      <path d="M98 20 h56 l24 26 v18 h-80 z"/>
    </g>
    <circle cx="114" cy="68" r="9" fill="var(--navy)" stroke="var(--white)" stroke-width="3"/>
    <circle cx="159" cy="68" r="9" fill="var(--navy)" stroke="var(--white)" stroke-width="3"/>
  </svg>
  <div class="abs promo-title big">DELIVERY</div>
  <div class="abs promo-title small">PROMO</div>

  <div class="abs app-tile" style="left:391px"><span>Hopmorsel</span></div>
  <div class="abs or script">or</div>
  <div class="abs app-tile" style="left:573px"><span>Vantrel</span></div>
  <div class="abs handle" style="left:333px">@hopmorsel<br>app</div>
  <div class="abs handle" style="left:515px">@vantrelcourier<br>app</div>

  <div class="abs receive">on <b>FRIDAYS</b> and receive:</div>
  <div class="abs pill">A&nbsp;<b>FREE</b>&nbsp;SAMPLE</div>
  <div class="abs sample-note">of our one of our <b>MEALPREP</b><br>meals in your bag!</div>

  <svg class="abs" style="left:0;top:375px" width="731" height="460" viewBox="0 0 731 460">
    <path d="M0 150 C 150 40, 380 10, 731 40 L731 460 L0 460 Z" fill="var(--green)"/>
    <path d="M0 128 C 150 25, 380 -5, 620 20" fill="none" stroke="var(--green-dark)" stroke-width="4"/>
  </svg>

  <div class="abs meals-photo" role="img" aria-label="Photo of meal prep containers with grilled meat, pasta and salad">
    <svg width="376" height="355" viewBox="0 0 376 355">
      <defs>
        <linearGradient id="mealTone" x1="0" y1="0" x2="1" y2="1">
          <stop offset="0" stop-color="#c9b98a"/>
          <stop offset=".5" stop-color="#8a5a3c"/>
          <stop offset="1" stop-color="#d8c79a"/>
        </linearGradient>
      </defs>
      <path d="M10 230 L150 110 L340 0 L376 10 L376 300 L250 355 L120 355 Z" fill="#1e2227"/>
      <path d="M30 230 L160 120 L340 15 L376 25 L376 290 L250 340 L130 340 Z" fill="url(#mealTone)" opacity=".85"/>
    </svg>
  </div>

  <div class="abs know script">Did You Know...</div>
  <div class="abs mealprep">MEAL<span>PREP</span></div>
  <div class="abs service">is another great service<br>that we offer!</div>

  <div class="abs benefit" style="left:40px">
    <div class="ring"><svg width="46" height="46" viewBox="0 0 46 46" fill="none" stroke="var(--navy)" stroke-width="2.5">
      <circle cx="23" cy="23" r="19"/><path d="M23 10 v13 l9 5"/></svg></div>
    <div class="label">SAVE<br>YOUR TIME</div>
  </div>
  <div class="abs benefit" style="left:164px">
    <div class="ring"><svg width="46" height="46" viewBox="0 0 46 46" fill="none" stroke="var(--navy)" stroke-width="2.5" stroke-linejoin="round">
      <path d="M23 38 C 8 27, 4 19, 8 12 C 12 5, 20 7, 23 13 C 26 7, 34 5, 38 12 C 42 19, 38 27, 23 38 Z"/>
      <path d="M6 23 h10 l3 -6 l4 12 l3 -6 h14"/></svg></div>
    <div class="label">PROMOTE<br>HEALTH</div>
  </div>
  <div class="abs benefit" style="left:288px">
    <div class="ring"><svg width="46" height="46" viewBox="0 0 46 46" fill="none" stroke="var(--navy)" stroke-width="2.5" stroke-linecap="round">
      <path d="M6 22 h34 c0 10 -7 17 -17 17 s-17 -7 -17 -17 z"/><path d="M17 16 c0 -4 4 -4 4 -8 M27 16 c0 -4 4 -4 4 -8"/></svg></div>
    <div class="label">DELICIOUS<br>LUNCH</div>
  </div>

  <div class="abs info-tab script">For more info:</div>

  <div class="abs brand">MARLOW PANTRY</div>
  <div class="abs brand-sub">HEALTHY KITCHEN &nbsp;|&nbsp; MEAL PREP</div>
  <div class="abs web">WWW.MARLOWPANTRY.EXAMPLE</div>
  <div class="abs social" style="left:472px" role="img" aria-label="Social profile"></div>
  <div class="abs social" style="left:519px" role="img" aria-label="Social profile"></div>

  <div class="abs footer-band">All orders are available for delivery or pickup!</div>
</main>
</body>
</html>
```